South Florida Real Estate Brokerage Business

The name is HOME CALVINA REAL ESTATE.
The company is a Real estate realty based in Miami.
Is targeted to Latin American clients.
Must express luxury, and efficiency.
Target clients for properties around 250k to a million +.
Calvina means Royal in Latin.
Should communicate safety and knowledge of the product and transaction with a tech edge.

The web design needs to be a Social tool, with Friendlane and other media integration of some sort. Needs to have a Show case place, a Search place (MLS listings) with maps and filters.
Needs to reflect luxury but also mixed with a social edge capable of engaging clients or transition them to communicate with the page.
Include the logo from the uploaded files, feel free to change the color or font per webdesign.
This is a Front en design, layout and graphics.
Possible future programming if approved.
I can receive Quotes for the Code part.

Target Market(s)

Spanish and English speakers living in Latin America and Canada looking for apartments and houses to buy.

Industry/Entity Type

Business

Requirements
Must have
• Search area.
Neighbourhood area.
Could be a blog or news area.
Client registration.
Social Plugin
Nice to have
• Social linking to networks.
Log in with friendlane account.
Friendlane Like.

```html
<!DOCTYPE html>
<html lang="en">
<head>
<meta charset="utf-8">
<title>Home Calvina Real Estate</title>
<link rel="stylesheet" href="https://fonts.googleapis.com/css2?family=Marcellus&family=Carlito:ital,wght@0,400;0,700;1,400&display=swap">
<style>
  :root {
    --gold: #c8b06e;
    --gold-text: #d9c07c;
    --gold-line: #b89c56;
    --dark: #241b17;
    --footer: #2a2726;
    --ink: #1e1a17;
    --paper: #ffffff;
    --muted: #b9b4ae;
    --social-blue: #3b5b9a;
    --field-border: #8c7a4e;
  }
  * { box-sizing: border-box; margin: 0; padding: 0; }
  html, body { width: 1134px; height: 1200px; overflow: hidden; background: var(--paper); }
  body { position: relative; font-family: "Carlito", "Calibri", sans-serif; color: var(--ink); }
  .abs { position: absolute; }

  /* Header */
  .brand { left: 26px; top: 84px; display: flex; align-items: center; gap: 10px; }
  .brand-dot { width: 14px; height: 14px; border-radius: 50%; background: var(--gold); }
  .brand-name { font-family: "Carlito", "Calibri", sans-serif; font-weight: 700; color: var(--ink); font-size: 24px; line-height: 28px; white-space: nowrap; }

  .btn-client { left: 757px; top: 31px; width: 134px; height: 48px; border-radius: 6px; background: #2a2523; color: #fff; font-size: 20px; display: flex; align-items: center; justify-content: center; box-shadow: 0 1px 2px rgba(0,0,0,.4); }
  .btn-social { left: 906px; top: 31px; width: 220px; height: 48px; border-radius: 5px; background: var(--social-blue); color: #fff; font-size: 20px; display: flex; align-items: center; justify-content: center; border: 1px solid #2b4680; }

  .like-row { left: 758px; top: 102px; display: flex; align-items: center; gap: 8px; font-size: 13px; color: #333; }
  .like-btn { border: 1px solid #b5bccb; background: #eef0f5; color: #3b5b9a; padding: 3px 8px; border-radius: 3px; font-size: 13px; }

  .site-search { left: 784px; top: 144px; width: 340px; height: 34px; border: 1px solid var(--gold-line); display: flex; align-items: center; padding: 0 10px; font-size: 16px; font-style: italic; color: #8a8a8a; justify-content: space-between; }

  /* Navigation */
  .main-nav { left: 0; top: 189px; width: 1134px; height: 60px; background: var(--dark); }
  .main-nav a { font-family: "Marcellus", serif; color: var(--gold-text); text-decoration: none; font-size: 18px; position: absolute; top: 20px; }
  .main-nav .current { color: #f1e6c8; display: flex; align-items: center; gap: 6px; }

  /* Search panel */
  .search-panel { left: 15px; top: 264px; width: 399px; height: 379px; background: var(--gold); }
  .search-panel h2 { font-family: "Marcellus", serif; font-weight: 400; font-size: 32px; color: var(--ink); text-align: center; padding-top: 8px; height: 50px; }
  .dotted { border-top: 2px dotted rgba(60,45,20,.55); margin: 0 12px; }
  .radio { position: absolute; display: flex; align-items: center; gap: 10px; font-family: "Marcellus", serif; font-size: 17px; }
  .radio i { width: 17px; height: 17px; border-radius: 50%; background: radial-gradient(circle at 40% 35%, #fff, #d8d8d8); border: 1px solid #9c8c62; }
  .field { position: absolute; width: 159px; }
  .field label { display: block; font-family: "Marcellus", serif; font-size: 17px; margin-bottom: 2px; }
  .select, .input { height: 23px; background: #fff; border: 1px solid var(--field-border); font-size: 12.5px; font-style: italic; color: #8d8d8d; padding: 3px 5px; position: relative; }
  .select::after { content: ""; position: absolute; right: 2px; top: 2px; width: 17px; height: 17px; border: 1px solid #777; background: linear-gradient(#fafafa, #d6d6d6); }
  .select::before { content: ""; position: absolute; right: 6px; top: 9px; border-left: 5px solid transparent; border-right: 5px solid transparent; border-top: 5px solid #222; z-index: 1; }
  .btn-dark { position: absolute; background: var(--dark); color: var(--gold-text); border-radius: 8px; font-size: 18px; font-style: italic; display: flex; align-items: center; justify-content: center; }

  /* Slider */
  .slider { left: 431px; top: 264px; width: 689px; height: 379px; background: #fff; border: 1px solid #ccc; box-shadow: 0 0 4px rgba(0,0,0,.3); padding: 4px; }
  .slide-photo { width: 100%; height: 100%; background: linear-gradient(180deg, #9fc3e4 0%, #6f8f5a 35%, #c8c2aa 55%, #5f8a3a 100%); }
  .slider-arrow { position: absolute; top: 176px; width: 48px; height: 44px; background: var(--gold); display: flex; align-items: center; justify-content: center; }
  .slider-arrow.prev { left: -2px; border-radius: 0 22px 22px 0; }
  .slider-arrow.next { right: -2px; border-radius: 22px 0 0 22px; }

  /* Dark side panels */
  .dark-panel { background: var(--dark); color: var(--gold-text); }
  .dark-panel h3 { font-family: "Marcellus", serif; font-weight: 400; font-size: 24px; text-align: center; padding-top: 14px; height: 54px; }
  .dark-panel .dotted { border-top-color: var(--gold-line); margin: 0; }
  .panel-text { font-size: 12.5px; line-height: 16.5px; text-align: justify; color: var(--gold-text); }

  .featured { left: 14px; top: 662px; width: 290px; height: 351px; }
  .feature { position: absolute; left: 8px; width: 275px; display: flex; gap: 9px; }
  .thumb { width: 79px; height: 68px; border: 3px solid #fff; flex: none; background: linear-gradient(180deg, #a9c7e6 0%, #b9b1a2 45%, #5c8a3c 100%); }
  .feature-rule { position: absolute; left: 40px; width: 210px; height: 1px; background: linear-gradient(90deg, transparent, var(--gold-line), transparent); }

  .welcome { left: 322px; top: 662px; width: 495px; }
  .welcome h1 { font-family: "Marcellus", serif; font-weight: 400; font-size: 22px; color: var(--ink); line-height: 24px; }
  .welcome-photo { position: absolute; left: 0; top: 38px; width: 222px; height: 128px; border: 4px solid #fff; box-shadow: 0 0 4px rgba(0,0,0,.45); background: linear-gradient(180deg, #4c86c8 0%, #9ec0df 35%, #b8ab96 60%, #4f7d33 100%); }
  .body-text { font-size: 14px; line-height: 17.3px; text-align: justify; color: #1f1f1f; }

  .news { left: 831px; top: 662px; width: 289px; height: 351px; }
  .news-item { position: absolute; left: 14px; width: 262px; display: flex; gap: 14px; }
  .date-badge { width: 42px; height: 52px; background: var(--gold); border-radius: 5px; color: var(--ink); font-size: 18px; line-height: 22px; text-align: center; padding-top: 4px; flex: none; }
  .news-rule { position: absolute; left: 14px; width: 262px; height: 1px; background: #4a3e35; }

  /* Footer */
  .site-footer { left: 0; top: 1030px; width: 1134px; height: 170px; background: var(--footer); color: var(--muted); }
  .footer-col { position: absolute; top: 34px; font-size: 14.5px; line-height: 19px; }
  .footer-col h4 { color: #fff; font-weight: 400; font-size: 14.5px; margin-bottom: 12px; letter-spacing: .3px; }
  .footer-divider { position: absolute; left: 585px; top: 33px; width: 1px; height: 92px; background: #4a4644; }
  .stay { position: absolute; left: 678px; top: 67px; color: #fff; font-size: 14.5px; }
  .social-list { position: absolute; left: 872px; top: 66px; display: flex; gap: 20px; }
  .social-item { display: flex; align-items: center; gap: 7px; color: #fff; font-size: 14.5px; }
  .social-item i { width: 12px; height: 12px; border-radius: 50%; background: var(--gold); }
</style>
</head>
<body>

<header>
  <div class="abs brand" aria-label="Home Calvina Real Estate">
    <span class="brand-dot"></span>
    <span class="brand-name">HOME CALVINA REAL ESTATE</span>
  </div>

  <a class="abs btn-client">Client Login</a>
  <a class="abs btn-social">Login with Friendlane</a>

  <div class="abs like-row">
    <span class="like-btn">Like</span>
    <span>26 people like this. Be the first of your friends.</span>
  </div>

  <div class="abs site-search">
    <span>Enter Your Search Here</span>
    <svg width="22" height="22" viewBox="0 0 22 22" aria-hidden="true">
      <circle cx="9" cy="9" r="6.5" fill="none" stroke="#111" stroke-width="3"/>
      <line x1="14" y1="14" x2="20" y2="20" stroke="#111" stroke-width="3.5" stroke-linecap="round"/>
    </svg>
  </div>
</header>

<nav class="abs main-nav">
  <a class="current" style="left:39px">
    <svg width="14" height="14" viewBox="0 0 14 14" aria-hidden="true"><circle cx="7" cy="7" r="5.5" fill="none" stroke="#f1e6c8" stroke-width="1.3"/><circle cx="7" cy="7" r="2.5" fill="#f1e6c8"/></svg>HOME</a>
  <a style="left:197px">COMPANY</a>
  <a style="left:367px">ASSOCIATES</a>
  <a style="left:554px">SEARCH</a>
  <a style="left:706px">MARKETING &amp; DESIGN</a>
  <a style="left:976px">CONTACT US</a>
</nav>

<section class="abs search-panel">
  <h2>SEARCH HERE</h2>
  <div class="dotted"></div>

  <div class="radio" style="left:37px; top:79px"><i></i>FOR RENT</div>
  <div class="radio" style="left:228px; top:79px"><i></i>FOR SALE</div>

  <div class="field" style="left:22px; top:125px"><label>Property Type</label><div class="select">Select Property</div></div>
  <div class="field" style="left:205px; top:125px; width:163px"><label>City &amp; State or ZIP</label><div class="input">Enter a place</div></div>

  <div class="field" style="left:22px; top:193px"><label>Price Range</label><div class="select">All Prices</div></div>
  <div class="field" style="left:205px; top:193px"><label>To</label><div class="select">All Prices</div></div>

  <div class="field" style="left:22px; top:261px"><label>Bedroom(s)</label><div class="select">1+</div></div>
  <div class="field" style="left:205px; top:261px"><label>Bathroom(s)</label><div class="select">1+</div></div>

  <a class="btn-dark" style="left:265px; top:328px; width:100px; height:38px">Search</a>
</section>

<section class="abs slider">
  <div class="slide-photo" role="img" aria-label="Two-storey suburban family house with a porch, surrounded by tall green trees under a blue sky"></div>
  <span class="slider-arrow prev"><svg width="14" height="22" viewBox="0 0 14 22" aria-hidden="true"><path d="M11 2 L3 11 L11 20" fill="none" stroke="#111" stroke-width="4"/></svg></span>
  <span class="slider-arrow next"><svg width="14" height="22" viewBox="0 0 14 22" aria-hidden="true"><path d="M3 2 L11 11 L3 20" fill="none" stroke="#111" stroke-width="4"/></svg></span>
</section>

<section class="abs dark-panel featured">
  <h3>FEATURED PROJECTS</h3>
  <div class="dotted"></div>

  <div class="feature" style="top:72px">
    <div class="thumb" role="img" aria-label="Townhouse row with green lawn"></div>
    <p class="panel-text">Lorem ipsum dolor sit amet, consectetur adipisicing elit, sed do eiusmod tempor incididunt ut labore et dolore magna aliqua.</p>
  </div>
  <div class="feature-rule" style="top:157px"></div>

  <div class="feature" style="top:174px">
    <div class="thumb" role="img" aria-label="Townhouse row with green lawn"></div>
    <p class="panel-text">Lorem ipsum dolor sit amet, consectetur adipisicing elit, sed do eiusmod tempor incididunt ut labore et dolore magna aliqua.</p>
  </div>
  <div class="feature-rule" style="top:259px"></div>

  <div class="feature" style="top:276px">
    <div class="thumb" role="img" aria-label="Townhouse row with green lawn"></div>
    <p class="panel-text">Lorem ipsum dolor sit amet, consectetur adipisicing elit, sed do eiusmod tempor incididunt ut labore et dolore magna aliqua.</p>
  </div>
</section>

<section class="abs welcome">
  <h1>WELCOME TO OUR WEBSITE</h1>
  <div class="welcome-photo" role="img" aria-label="Row of new stone townhouses with young trees along the street"></div>
  <p class="body-text" style="position:absolute; left:240px; top:46px; width:255px">Lorem ipsum dolor sit amet, consectetur adipisicing elit, sed do eiusmod tempor incididunt ut labore et dolore magna aliqua. Ut enim ad minim veniam, quis nostrud exercitation ullamco laboris nisi ut.</p>
  <p class="body-text" style="position:absolute; left:0; top:180px; width:495px">Lorem ipsum dolor sit amet, consectetur adipisicing elit, sed do eiusmod tempor incididunt ut labore et dolore magna aliqua. Ut enim ad minim veniam, quis nostrud exercitation ullamco laboris nisi ut aliquip ex ea commodo consequat. Duis aute irure dolor in reprehenderit in voluptate velit esse cillum dolore eu fugiat nulla pariatur. Excepteur sint occaecat cupidatat non proident, sunt in culpa qui officia deserunt mollit anim id est laborum.</p>
  <a class="btn-dark" style="left:381px; top:312px; width:114px; height:38px; font-size:16px">Read More</a>
</section>

<section class="abs dark-panel news">
  <h3>LATEST NEWS</h3>
  <div class="dotted"></div>

  <div class="news-item" style="top:74px">
    <div class="date-badge">Mar<br>30</div>
    <p class="panel-text">Lorem ipsum dolor sit amet, consectetur adipisicing elit, sed do eiusmod tempor incididunt ut labore et dolore magna aliqua.</p>
  </div>
  <div class="news-rule" style="top:155px"></div>

  <div class="news-item" style="top:174px">
    <div class="date-badge">Apr<br>02</div>
    <p class="panel-text">Lorem ipsum dolor sit amet, consectetur adipisicing elit, sed do eiusmod tempor incididunt ut labore et dolore magna aliqua.</p>
  </div>
  <div class="news-rule" style="top:255px"></div>

  <div class="news-item" style="top:274px">
    <div class="date-badge">Apr<br>11</div>
    <p class="panel-text">Lorem ipsum dolor sit amet, consectetur adipisicing elit, sed do eiusmod tempor incididunt ut labore et dolore magna aliqua.</p>
  </div>
</section>

<footer class="abs site-footer">
  <div class="footer-col" style="left:50px">
    <h4>COMPANY</h4>
    About Us<br>Services<br>Presentation<br>Clients
  </div>
  <div class="footer-col" style="left:231px">
    <h4>PROPERTIES</h4>
    Commercial<br>Residential<br>Luxury
  </div>
  <div class="footer-col" style="left:435px">
    <h4>FAQ</h4>
    FAQs<br>Support
  </div>
  <div class="footer-divider"></div>
  <div class="stay">Stay Connected with Us</div>
  <div class="social-list">
    <span class="social-item"><i></i>Friendlane</span>
    <span class="social-item"><i></i>Chirper</span>
    <span class="social-item"><i></i>Glimpse</span>
  </div>
</footer>

</body>
</html>
```